Golden Years Wellness Roadmap: This is my second book. The first was Eldercare Compass

I need a book cover design for: GOLDEN YEARS WELLNESS ROADMAP: A NO-EXPENSE METHOD FOR FINISHING YOUR LATER-LIFE MOSAIC WITH POOLED KVB CARE SCHEMES by Derek Holloway Neil Osgrove & Martin Quarles. This book is designed for business owners, CEO's, CFO's and Human Resources. The cover needs to be professional and focused on business. The purpose of this book is to educate business owners and their management about a zero cost retiree health plan. This is a first of it's kind solution that every business needs to learn about.

Target Market(s)

Business owners, CEO's, CFO's and Human Resources

Requirements
Nice to have
• I want the design to be clean and professional since it is focused on business executives

```html
<!DOCTYPE html>
<html lang="en">
<head>
<meta charset="utf-8">
<title>Golden Years Wellness Roadmap — Book Cover</title>
<link href="https://fonts.googleapis.com/css2?family=Bebas+Neue&family=Space+Mono:wght@700&family=Cinzel:wght@400&display=swap" rel="stylesheet">
<style>
  :root {
    --ink-light: #fbf8f1;
    --night-deep: #0e1c2a;
    --night-mid: #1d3346;
    --steel: #5f7284;
    --shirt-blue: #8fb0cf;
    --desk-dark: #2a2a30;
    --glow-cyan: #5fd6e6;
  }
  * { margin: 0; padding: 0; box-sizing: border-box; }
  html, body {
    width: 843px;
    height: 1200px;
    overflow: hidden;
    background: var(--night-deep);
  }
  .cover {
    position: relative;
    width: 843px;
    height: 1200px;
    overflow: hidden;
  }
  .cover-scene {
    position: absolute;
    inset: 0;
    background:
      radial-gradient(ellipse 260px 360px at 720px 640px, rgba(143,176,207,0.55), transparent 70%),
      radial-gradient(ellipse 230px 300px at 430px 720px, rgba(150,160,170,0.45), transparent 70%),
      radial-gradient(ellipse 300px 260px at 200px 700px, rgba(95,214,230,0.22), transparent 70%),
      radial-gradient(ellipse 200px 120px at 90px 280px, rgba(230,190,120,0.18), transparent 70%),
      linear-gradient(180deg, var(--night-deep) 0%, var(--night-mid) 45%, var(--steel) 72%, var(--desk-dark) 100%);
  }
  .cover-text {
    position: relative;
    z-index: 1;
    text-align: center;
    color: var(--ink-light);
  }
  .title {
    padding-top: 78px;
    font-family: 'Bebas Neue', sans-serif;
    font-weight: 400;
    font-size: 158px;
    line-height: 124px;
    letter-spacing: 1px;
  }
  .title span { display: block; }
  .subtitle {
    margin-top: 22px;
    font-family: 'Space Mono', monospace;
    font-weight: 700;
    font-size: 25px;
    line-height: 40px;
    letter-spacing: 0.5px;
  }
  .subtitle span { display: block; }
  .authors {
    position: absolute;
    left: 0;
    right: 0;
    top: 1068px;
    font-family: 'Cinzel', serif;
    font-size: 27px;
    line-height: 32px;
  }
  .authors span { display: block; }
</style>
</head>
<body>
  <main class="cover">
    <div class="cover-scene" role="img" aria-label="Photograph of two business professionals at a desk with a laptop and notebooks, overlaid with glowing hexagonal network icons, against a night-time city office backdrop"></div>
    <div class="cover-text">
      <h1 class="title">
        <span>Golden Years</span>
        <span>Wellness</span>
        <span>Roadmap</span>
      </h1>
      <p class="subtitle">
        <span>A NO-EXPENSE METHOD FOR</span>
        <span>FINISHING YOUR LATER-LIFE MOSAIC</span>
        <span>WITH POOLED KVB CARE SCHEMES</span>
      </p>
    </div>
    <p class="authors cover-text">
      <span>Derek Holloway</span>
      <span>Neil Osgrove &amp; Martin Quarles</span>
    </p>
  </main>
</body>
</html>
```